Create an awesome website for a medical clinic

This is a new website for a doctor's office. The site should be clean and modern, easy to navigate.

This is a wellness clinic, we want to help our clients have a healthy, active lifestyle. It should be friendly and inviting, and easy for them to call or schedule an appointment.

The site should be responsive and designed using the attached Bootstrap 3 PSD.

We will provide stock photos, until then please use stock photos from:

photoharvestbin.net or
lumapicturevault.net (preferred)

Some example sites of clean and modern designs that we like:

https://tarnelspine.example/
http://walkpastjoints.example/
http://feelingbrisker.example/

Also attached is a temporary logo you can use.
Updates

Reason: Thank you everyone for your great designs - we need a little more time so I'm extending the project.

Need extra days to review

Also, the colors in the new logo I just linked to are the final colors of the logo, so feel free to use any complimentary colors to it.

Hi everyone, The boss wants to change the layout of the site a little bit - here's the revised layout: https://www.filecrate.example/s/q8vn31kd2pxe74rt/memo%2011_29_2017.pdf?dl=0 And the graphic assets you can use are here: https://www.filecrate.example/s/q8vn31kd2pxe74rt/memo%2011_29_2017.pdf?dl=0 Feel free to change the background color of the "topbar", and change the icons of the "why people trust us" if you want, these are just temporary placeholders. Thanks for your patience and hard work!

Target Market(s)

People seeking medical treatment (wellness clinic)

Industry/Entity Type

Doctor

Number of Pages Required

1 page

Font styles to use
Sans Serif

Colors
0592cd
33a6d7
abd037
9bcb3c

Requirements
Must have
• The home page should have: a strong hero image/slideshow, clinic phone number should be prominent and at the top of the page (in the nav), a "what to expect" section (this is like a FAQs section - see attachment), and a strong call to action (a button to call or schedule an appointment).
• The what to expect section is useful so that prospective clients can determine if we're a good fit for them or not. It's a basic, first-step pre-qualification block of information.
• Social media icons which links to our social media profiles should be included.
Nice to have
• - Link to 3 most recent blog entries
• - Testimonials
• - How a multilevel nav menu looks.

```html
<!DOCTYPE html>
<html lang="en">
<head>
<meta charset="utf-8">
<title>Wellness Clinic</title>
<link href="https://fonts.googleapis.com/css2?family=Roboto:wght@300;400;500;700&display=swap" rel="stylesheet">
<style>
:root{
  --blue:#33a6d7;
  --blue-deep:#0592cd;
  --green:#9bcb3c;
  --ink:#4a4f55;
  --muted:#9aa0a6;
  --line:#e3e6e9;
  --footer:#6b7178;
  --footer-text:#e8ebee;
  --bar:#5e646b;
  --white:#ffffff;
}
*{box-sizing:border-box;margin:0;padding:0}
html,body{width:1200px;height:3104px;overflow:hidden}
body{position:relative;background:var(--white);font-family:"Roboto",Arial,sans-serif;color:var(--ink)}
.abs{position:absolute}
.photo{position:absolute;border-radius:4px}
.visit-title{font-size:18px;font-weight:500;color:#5a5f65}
.visit-text{font-size:14.5px;line-height:23px;color:var(--muted);font-weight:300;width:500px;margin-top:8px}
.testimonials{top:639px;left:0;width:1200px;height:492px;background:linear-gradient(90deg,#c9c6c2 0%,#b8b4ae 30%,#a9a7a2 60%,#c2c0bc 100%)}
.testimonials::after{content:"";position:absolute;inset:0;background:rgba(70,72,76,.35)}
.section-title{position:absolute;left:0;width:1200px;text-align:center;font-size:21px;font-weight:400;letter-spacing:.5px}
.down-arrow{position:absolute;left:588px}
.quote{position:absolute;z-index:2;top:872px;left:310px;width:580px;text-align:center;color:#f4f4f4;font-size:15px;line-height:24px;font-weight:300}
.quote-mark{position:absolute;z-index:2;top:862px;font-size:70px;line-height:70px;color:#f4f4f4;font-family:Georgia,serif;font-weight:700}
.author{position:absolute;z-index:2;top:958px;left:0;width:1200px;text-align:center;color:#f4f4f4;font-size:15px}
.dots{position:absolute;z-index:2;top:1013px;left:573px;display:flex;gap:8px}
.dots span{width:22px;height:22px;border:2px solid #eee}
.card{position:absolute;top:1368px;width:316px;height:334px;background:#fff;box-shadow:0 1px 6px rgba(0,0,0,.12)}
.card .thumb{height:141px}
.card h3{font-size:15px;font-weight:400;color:#555;margin:32px 26px 0}
.card p{font-size:12px;line-height:18px;color:#a5abb0;margin:12px 26px 0;font-weight:300}
.card .more{display:block;font-size:12px;color:var(--blue);margin:14px 26px 0}
.contact-form{position:absolute;top:1806px;left:725px;width:318px;height:430px;background:#fff;box-shadow:0 2px 12px rgba(0,0,0,.18);padding:46px 38px 0}
.contact-form h2{font-size:20px;font-weight:400;color:#6a7076;text-align:center;margin-bottom:22px}
.field{height:31px;border:1px solid var(--line);font-size:10px;color:#b3b8bd;padding:9px 10px;margin-bottom:13px}
.field.area{height:104px}
.send{height:30px;background:var(--blue);color:#fff;font-size:11px;text-align:center;line-height:30px}
.footer{top:2315px;left:0;width:1200px;height:390px;background:var(--footer);color:var(--footer-text)}
.social{position:absolute;top:43px;width:30px;height:30px;border:1.5px solid #e3e6e9;border-radius:50%}
.info{position:absolute;top:40px;display:flex;gap:14px;align-items:flex-start}
.info .ic{width:34px;height:34px;border-radius:50%;display:flex;align-items:center;justify-content:center}
.info b{display:block;font-size:13px;font-weight:500;color:#fff}
.info span{font-size:12px;color:#dfe3e6}
.divider{position:absolute;top:114px;left:100px;width:1000px;height:1px;background:rgba(255,255,255,.12)}
.col{position:absolute;top:158px;font-size:12px;line-height:21px}
.col h4{font-size:13.5px;font-weight:500;color:#fff;margin-bottom:10px}
.hours{width:228px}
.hours div{display:flex;justify-content:space-between}
.hours small{font-size:10.5px}
.hours .today{font-weight:700;color:#fff}
.map{top:2705px;left:0;width:1200px;height:351px;background:linear-gradient(180deg,#eef0f2,#e4e7ea)}
.bottom-bar{top:3056px;left:0;width:1200px;height:48px;background:var(--bar)}
</style>
</head>
<body>

<!-- Visits -->
<div class="photo" role="img" aria-label="Doctor in white coat with stethoscope and colleagues examining a patient" style="top:17px;left:100px;width:402px;height:232px;background:linear-gradient(120deg,#cfe1ee,#eef3f6 55%,#d6e4ee)"></div>
<div class="abs" style="top:58px;left:612px">
  <div class="visit-title">Visit 3</div>
  <p class="visit-text">Lorem ipsum dolor sit amet, consectetur adipiscing elit, sed do eiusmod tempor incididunt ut labore et dolore magna aliqua. Ut enim ad minim veniam, quis nostrud exercitation ullamco laboris nisi ut aliquip ex ea commodo consequat. But I must explain to you how all this mistaken idea of denouncing pleasure.</p>
</div>
<div class="abs" style="top:334px;left:100px">
  <div class="visit-title">Visit 4</div>
  <p class="visit-text">Lorem ipsum dolor sit amet, consectetur adipiscing elit, sed do eiusmod tempor incididunt ut labore et dolore magna aliqua. Ut enim ad minim veniam, quis nostrud exercitation ullamco laboris nisi ut aliquip ex ea commodo consequat. But I must explain to you how all this mistaken idea of denouncing pleasure.</p>
</div>
<div class="photo" role="img" aria-label="Smiling team of doctors and nurses in scrubs" style="top:291px;left:696px;width:404px;height:234px;background:linear-gradient(120deg,#e9eef1,#d3e2ea 50%,#eef2f4)"></div>

<!-- Testimonials -->
<section class="abs testimonials" role="img" aria-label="Blurred photo of a happy patient giving a thumbs up next to a doctor"></section>
<h2 class="section-title" style="top:731px;color:#fff;z-index:2">WHAT OTHERS ARE SAYING</h2>
<svg class="down-arrow" style="top:778px;z-index:2" width="24" height="30" viewBox="0 0 24 30"><path d="M12 1v27M2 18l10 10 10-10" fill="none" stroke="#fff" stroke-width="1.5"/></svg>
<div class="quote-mark" style="left:243px">&ldquo;</div>
<p class="quote">Sed ut perspiciatis unde omnis iste natus error sit voluptatem accus adoloremque laudantium, totam rem aperiam, eaque ipsa quae ab illo inventore veritatis et quasi architecto beatae</p>
<div class="quote-mark" style="left:912px">&rdquo;</div>
<div class="author"><b style="font-weight:500">Mira Holt,</b> sport trainer</div>
<div class="dots"><span></span><span></span></div>

<!-- Blog -->
<h2 class="section-title" style="top:1223px;color:#6a7076">LATEST NEWS FROM OUR BLOG</h2>
<svg class="down-arrow" style="top:1270px" width="24" height="30" viewBox="0 0 24 30"><path d="M12 1v27M2 18l10 10 10-10" fill="none" stroke="#33a6d7" stroke-width="1.5"/></svg>

<article class="card" style="left:100px">
  <div class="thumb" role="img" aria-label="Doctor typing on a computer keyboard" style="background:linear-gradient(120deg,#e3ecf2,#f6f7f8 50%,#d9c8b5)"></div>
  <h3>Lorem ipsum dolor set amet</h3>
  <p>Sed ut perspiciatis unde omnis iste natus error sit voluptatem accusantium doloremque laudantium, totam rem aperiam, eaque ipsa quae ab illo inventore veritatis et quasi</p>
  <span class="more">MORE &nbsp;&rsaquo;</span>
</article>
<article class="card" style="left:442px">
  <div class="thumb" role="img" aria-label="Smiling senior doctor with medical colleagues" style="background:linear-gradient(120deg,#cfe2ea,#eef2f4 55%,#d7e3ea)"></div>
  <h3>Lorem ipsum dolor set amet</h3>
  <p>Sed ut perspiciatis unde omnis iste natus error sit voluptatem accusantium doloremque laudantium, totam rem aperiam, eaque ipsa quae ab illo inventore veritatis et quasi</p>
  <span class="more">MORE &nbsp;&rsaquo;</span>
</article>
<article class="card" style="left:785px">
  <div class="thumb" role="img" aria-label="Doctor examining a young child" style="background:linear-gradient(120deg,#f3efea,#e7d6cb 50%,#eef2ea)"></div>
  <h3>Lorem ipsum dolor set amet</h3>
  <p>Sed ut perspiciatis unde omnis iste natus error sit voluptatem accusantium doloremque laudantium, totam rem aperiam, eaque ipsa quae ab illo inventore veritatis et quasi</p>
  <span class="more">MORE &nbsp;&rsaquo;</span>
</article>

<!-- Contact -->
<svg class="abs" style="top:1806px;left:0" width="1200" height="509" viewBox="0 0 1200 509">
  <defs><linearGradient id="contactBand" x1="0" x2="1" y1="0" y2="0"><stop offset="0" stop-color="#a9abae"/><stop offset=".6" stop-color="#c8cacc"/><stop offset="1" stop-color="#8f9296"/></linearGradient></defs>
  <polygon points="0,156 1200,0 1200,509 0,509" fill="url(#contactBand)"/>
</svg>
<div class="photo" role="img" aria-label="Young doctor with stethoscope pointing toward the message form" style="top:1827px;left:104px;width:580px;height:488px;border-radius:0;background:radial-gradient(ellipse at 40% 55%,#f1f3f5 0%,#dfe6ec 45%,rgba(200,202,204,0) 75%)"></div>
<form class="contact-form">
  <h2>Send us a Message</h2>
  <div class="field">Full Name</div>
  <div class="field">Phone number</div>
  <div class="field">Email Address</div>
  <div class="field area">Type your message</div>
  <div class="send">Send Message</div>
</form>

<!-- Footer -->
<footer class="abs footer">
  <span class="social" style="left:100px"></span>
  <span class="social" style="left:141px"></span>
  <span class="social" style="left:182px"></span>

  <div class="info" style="left:357px">
    <div class="ic" style="background:var(--blue)"><svg width="14" height="18" viewBox="0 0 14 18"><path d="M7 1a6 6 0 0 0-6 6c0 4.5 6 10 6 10s6-5.5 6-10a6 6 0 0 0-6-6z" fill="#fff"/><circle cx="7" cy="7" r="2.2" fill="#33a6d7"/></svg></div>
    <div><b>Our Address</b><span>418 Harrow Bend Lane</span></div>
  </div>
  <div class="info" style="left:612px">
    <div class="ic" style="background:var(--green)"><svg width="18" height="18" viewBox="0 0 18 18"><circle cx="9" cy="9" r="7.5" fill="#fff"/><path d="M9 4.5V9l3 2" fill="none" stroke="#9bcb3c" stroke-width="1.6"/></svg></div>
    <div><b>Open Hours</b><span>Mon - Friday: 8AM - 5PM</span></div>
  </div>
  <div class="info" style="left:870px">
    <div class="ic" style="background:var(--blue)"><svg width="16" height="16" viewBox="0 0 16 16"><path d="M3.5 1.5l2.5 3-1.6 1.6a9 9 0 0 0 5.5 5.5l1.6-1.6 3 2.5-1.5 2A11.5 11.5 0 0 1 1.5 3z" fill="#fff"/></svg></div>
    <div><b>Give us a Call</b><span>+(10)555 - 014 - 2278</span></div>
  </div>

  <div class="divider"></div>

  <div class="col" style="left:100px;width:200px">
    <h4>About us</h4>
    <p style="line-height:17px">Sed ut perspiciatis unde omnis iste natus error sit voluptatem accu santium doloremque laudantium, totam rem veritatis et quasi</p>
  </div>
  <div class="col" style="left:357px">
    <h4>Navigation</h4>
    <div>Home</div><div>About</div><div>Services</div><div>Blog</div><div>Contact us</div>
  </div>
  <div class="col" style="left:612px">
    <h4>Services</h4>
    <div>Lorem ipsum</div><div>Set amet</div><div>Dolor lorem</div><div>Omnis iste</div>
  </div>
  <div class="col hours" style="left:872px">
    <h4>Working Hours</h4>
    <div><span>Monday</span><small>08:00 - 17:00</small></div>
    <div><span>Tuesday</span><small>08:00 - 17:00</small></div>
    <div><span>Wednesday</span><small>08:00 - 17:00</small></div>
    <div class="today"><span>Thursday</span><small>08:00 - 17:00</small></div>
    <div><span>Friday</span><small>08:00 - 17:00</small></div>
    <div><span>Saturday</span><small>10:00 - 16:00</small></div>
    <div><span>Sunday</span><small>Closed</small></div>
  </div>
</footer>

<!-- Map -->
<div class="abs map" role="img" aria-label="Street map of the clinic's city area"></div>
<svg class="abs" style="top:2800px;left:580px" width="36" height="48" viewBox="0 0 36 48"><path d="M18 2A15 15 0 0 0 3 17c0 11 15 29 15 29s15-18 15-29A15 15 0 0 0 18 2z" fill="#33a6d7"/><circle cx="18" cy="17" r="5.5" fill="#fff"/></svg>

<div class="abs bottom-bar"></div>
<svg class="abs" style="top:3020px;left:553px" width="94" height="47" viewBox="0 0 94 47"><path d="M0 47a47 47 0 0 1 94 0z" fill="#5e646b"/><path d="M33 34l14-13 14 13" fill="none" stroke="#fff" stroke-width="2"/></svg>

</body>
</html>
```